Birchwell Chiropractic, achieve your health goals, get better each day one step at a time

A mobile friendly site, fresh look, easy to navigate, has interface with zq/chirplane, etc. Blog posts. Uses new logo. Content and address to current site is marvintoque.com. The current site will give you scope of project for content. The logo is not the final but close. Will upload final next week.
Convey the concept that heath is a process, it does not just happen. We take steps to achieve what we want in life including health.

Target Market(s)

30 to 70 year old. Needing health care

Industry/Entity Type

Health Care

Coding

Coded - Design and coding required

Number of Pages Required

5+ page

Font styles to use
Sans Serif

Colors

Designer to choose colors to be used in the design.

Requirements
Must have
• mobile friendly, easy to navigate, ZQ/Chirplane interface, blog, room for current content
Nice to have
• potential for commerce, statistics
Should not have
• Same old look and feel as everything else out there

```html
<!DOCTYPE html>
<html lang="en">
<head>
<meta charset="utf-8">
<title>Birchwell Chiropractic</title>
<link rel="stylesheet" href="https://fonts.googleapis.com/css2?family=Michroma&family=Open+Sans:ital,wght@0,400;0,600;0,700;1,700&display=swap">
<style>
:root{
  --blue:#2e75b6;
  --blue-dark:#1f5d96;
  --green:#8cc63f;
  --green-dark:#74ad2a;
  --ink:#333b44;
  --muted:#7a828b;
  --light:#f1f3f5;
  --white:#ffffff;
  --skin:#e4bfa6;
  --skin-dark:#b98a6e;
}
*{box-sizing:border-box;margin:0;padding:0}
html,body{width:1200px;height:4800px;overflow:hidden}
body{position:relative;background:var(--white);font-family:"Open Sans",Arial,sans-serif;color:var(--ink);font-size:13px;line-height:1.5}
.abs{position:absolute}
.display{font-family:"Michroma","Open Sans",sans-serif;letter-spacing:1px}
.ph{background:linear-gradient(135deg,#f0dccd 0%,var(--skin) 45%,#8fa9bf 100%)}
.ph.b{background:linear-gradient(135deg,#dfe7ee 0%,#e8c7b0 50%,var(--skin-dark) 100%)}
.ph.g{background:linear-gradient(135deg,#c7dd9a 0%,#7fa64a 55%,#efe9df 100%)}

/* top bar and nav */
.topbar{left:0;top:0;width:1200px;height:26px;background:var(--blue);color:var(--white);font-size:11px}
.topbar .info{left:660px;top:5px;display:flex;gap:22px;align-items:center}
.topbar .dot{width:13px;height:13px;border-radius:50%;background:rgba(255,255,255,.85);display:inline-block}
.nav{left:0;top:26px;width:1200px;height:70px;background:var(--white);box-shadow:0 2px 6px rgba(0,0,0,.08);z-index:3}
.brand{left:210px;top:20px;display:flex;align-items:center;gap:8px;font-weight:700;font-size:22px;color:var(--blue)}
.brand i{width:22px;height:22px;background:var(--green);border-radius:50%;display:block}
.menu{left:490px;top:26px;display:flex;gap:34px;font-size:11px;font-weight:600;color:var(--ink);text-transform:uppercase}
.menu .on{color:var(--green);border-bottom:2px solid var(--green);padding-bottom:4px}

/* hero */
.hero{left:0;top:96px;width:1200px;height:600px;overflow:hidden}
.hero .photo{left:0;top:0;width:1200px;height:600px;background:linear-gradient(90deg,#cbd7e1 0%,#f4f6f8 10%,#dcb79e 22%,#eef1f4 32%,#c9967b 42%,#e3eaf0 56%,#f3f6f9 100%)}
.hero h1{left:640px;top:136px;font-size:46px;font-weight:700;font-style:italic;color:var(--blue);text-transform:uppercase;letter-spacing:1px}
.hero h2{left:660px;top:196px;font-size:34px;font-weight:700;font-style:italic;color:var(--green);text-transform:uppercase;display:flex;align-items:center;gap:14px}
.hero h2::before,.hero h2::after{content:"";width:44px;height:3px;background:var(--green)}
.hero .tag{left:706px;top:252px;font-size:19px;font-weight:700;font-style:italic;color:var(--blue-dark)}
.btn{display:inline-block;background:var(--blue);color:var(--white);font-size:11px;font-weight:700;text-transform:uppercase;padding:9px 22px;letter-spacing:.5px}
.hero .btn{left:760px;top:296px;transform:skewX(-12deg)}
.arrow{width:30px;height:30px;color:rgba(255,255,255,.9)}

/* section titles */
.title{width:1200px;left:0;text-align:center}
.title h3{font-size:22px;color:var(--blue);display:flex;justify-content:center;align-items:center;gap:14px}
.title h3::before,.title h3::after{content:"";width:46px;height:2px;background:var(--green)}
.title h3 span{color:var(--green)}
.title p{font-size:11px;color:var(--muted);margin-top:6px}

/* welcome */
.welcome-kicker{font-size:15px;color:var(--green)}
.welcome-copy{left:212px;top:790px;width:385px}
.welcome-copy h4{font-size:13px;font-weight:700;text-transform:uppercase;color:var(--ink);line-height:1.35;margin-bottom:10px}
.welcome-copy p{font-size:11px;color:var(--muted);margin-bottom:12px}
.video{left:620px;top:790px;width:372px;height:245px;background:linear-gradient(135deg,#3a4652 0%,#8a9aa8 45%,#c0765a 62%,#4b5866 100%);box-shadow:0 4px 14px rgba(0,0,0,.25)}
.video .bar{left:0;bottom:0;width:100%;height:26px;background:#22292f}
.video .play{left:160px;top:95px;width:50px;height:50px;border-radius:50%;background:var(--green)}

/* services */
.services-bg{left:0;top:1090px;width:1200px;height:820px}
.services-people{left:0;top:1100px;width:1200px;height:760px;background:linear-gradient(90deg,rgba(228,191,166,.25),rgba(46,117,182,0) 30%,rgba(46,117,182,0) 70%,rgba(228,191,166,.3))}
.services .card{width:240px;height:190px;overflow:hidden;background:#c6d2dc}
.services .card .ph{width:100%;height:164px}
.services .card span{display:block;height:26px;background:var(--green);color:var(--white);text-align:center;font-size:12px;font-weight:700;line-height:26px;text-transform:uppercase}
.btn-ghost{border:2px solid var(--white);color:var(--white);font-size:11px;font-weight:700;padding:6px 20px;text-transform:uppercase}

/* conditions */
.cond-circle{left:448px;top:2048px;width:320px;height:320px;border-radius:50%;background:radial-gradient(circle at 50% 45%,#f3c9a8 0%,#e58a5a 22%,#d9b7a0 38%,#6f98c2 62%,var(--blue) 100%)}
.cond{font-size:13px;font-weight:700;color:var(--ink);text-transform:uppercase;display:flex;align-items:center;gap:14px}
.cond i{width:38px;height:38px;border-radius:50%;background:var(--green);display:block;position:relative;border:3px solid var(--white)}
.cond i::after{content:"";position:absolute;left:11px;top:7px;width:10px;height:18px;border:2px solid var(--white);border-radius:5px}

/* testimonials */
.testi-bg{left:330px;top:2460px;width:870px;height:210px;background:var(--light)}
.testi-family{left:0;top:2440px;width:340px;height:250px;background:linear-gradient(135deg,#f0d8c4 0%,var(--skin) 40%,#6d8fb3 100%)}
.testi-title{left:410px;top:2500px;font-size:22px;color:var(--green);display:flex;align-items:center;gap:12px}
.testi-title b{font-weight:400;color:var(--blue)}
.testi-title::before,.testi-title::after{content:"";width:40px;height:2px;background:var(--green)}
.quote{width:270px;display:flex;gap:12px;align-items:flex-start}
.quote .avatar{width:48px;height:54px;flex:none;background:linear-gradient(135deg,#d9b49b,#7f8d9a)}
.quote p{font-size:10px;font-style:italic;color:var(--muted)}
.quote small{display:block;font-size:10px;font-weight:700;color:var(--blue);margin-top:6px}
.quote small em{color:#f2b318;font-style:normal;margin-left:6px}

/* doctor */
.doc-photo{left:232px;top:2760px;width:228px;height:250px;background:linear-gradient(135deg,#d8c3b2 0%,#a78570 45%,#4a5561 100%)}
.doc-caption{left:232px;top:3010px;width:228px;height:42px;background:var(--green);color:var(--white);font-size:10px;font-weight:700;text-align:center;line-height:42px;text-transform:uppercase}
.doc h3{font-size:24px;color:var(--green);display:flex;align-items:center;gap:14px}
.doc h3::after{content:"";width:46px;height:2px;background:var(--green)}
.doc h3 b{font-weight:400;color:var(--blue)}
.doc h5{font-size:11px;font-weight:700;color:var(--ink);text-transform:uppercase;margin-top:14px}
.doc p{font-size:10px;color:var(--muted)}
.edu{display:flex;gap:12px;margin-top:8px}
.edu div{width:108px;height:62px;background:#e1ecf6;color:var(--blue);font-size:8px;font-weight:700;text-transform:uppercase;text-align:center;padding:10px 6px;line-height:1.3}

/* blog */
.blog-bg{left:0;top:3080px;width:1200px;height:600px}
.post{width:240px;height:310px;background:var(--white);box-shadow:0 3px 10px rgba(0,0,0,.15)}
.post .ph{height:150px;position:relative}
.post .date{position:absolute;right:10px;top:0;width:42px;height:46px;background:var(--blue);color:var(--white);text-align:center;font-weight:700;font-size:18px;line-height:1.1;padding-top:6px}
.post .date small{display:block;font-size:9px;font-weight:600}
.post h6{font-size:12px;font-weight:700;color:var(--ink);padding:14px 14px 6px;line-height:1.35}
.post p{font-size:10px;color:var(--muted);padding:0 14px}

/* social */
.social h4{font-size:17px;color:var(--blue);display:flex;align-items:center;gap:10px}
.social h4 i{width:18px;height:18px;background:var(--blue);display:block}
.social h4::after{content:"";width:46px;height:2px;background:var(--green)}
.widget{width:372px;height:320px;border:1px solid #dde2e7;background:var(--white);overflow:hidden}
.widget .head{height:58px;background:linear-gradient(135deg,#5c6b78,#c9a48c);color:var(--white);font-size:12px;font-weight:700;padding:12px 14px}
.widget .row{padding:12px 14px;border-bottom:1px solid #eceff2;font-size:10px;color:var(--muted)}
.widget .row b{color:var(--ink);font-size:11px}

/* footer */
.map{left:0;top:4160px;width:1200px;height:220px;background:linear-gradient(180deg,#e9e7e1,#f2f0ea 50%,#e7d9a8)}
.footer-bg{left:0;top:4320px;width:1200px;height:480px}
.fcol{color:var(--white);font-size:11px}
.fcol h5{font-size:12px;font-weight:700;text-transform:uppercase;margin-bottom:14px;letter-spacing:.5px}
.fcol li{list-style:none;margin-bottom:7px}
.fcol li::before{content:"› ";color:var(--green)}
.fcol .ci{display:flex;gap:8px;margin-bottom:10px;align-items:flex-start}
.fcol .ci svg{flex:none;margin-top:2px}
.hours td{padding:1px 16px 3px 0}
.hours td:nth-child(2){color:var(--white);font-weight:600}
.f-brand{font-weight:700;font-size:20px;display:flex;gap:8px;align-items:center}
.f-brand i{width:20px;height:20px;border-radius:50%;background:var(--green);display:block}
.circles{display:flex;gap:8px;margin-top:14px}
.circles i{width:22px;height:22px;border-radius:50%;background:var(--white);display:block}
.copyright{left:0;top:4768px;width:1200px;text-align:center;color:rgba(255,255,255,.8);font-size:9px;text-transform:uppercase}
</style>
</head>
<body>

<div class="abs topbar">
  <div class="abs info">
    <span>555-0142</span>
    <span>info@marvintoque.com</span>
    <span class="dot"></span><span class="dot"></span><span class="dot"></span>
  </div>
</div>

<header class="abs nav">
  <div class="abs brand"><i></i>Birchwell</div>
  <nav class="abs menu">
    <span class="on">Home</span><span>Health Services ▾</span><span>About ▾</span><span>New Patients</span><span>Contact</span>
  </nav>
</header>

<section class="abs hero">
  <div class="abs photo" role="img" aria-label="Smiling chiropractor in white coat holding a spine model beside a female patient"></div>
  <h1 class="abs">Achieve Your</h1>
  <h2 class="abs">Health Goals</h2>
  <p class="abs tag">Get better each day one step at a time</p>
  <span class="abs btn">Schedule an Appointment</span>
  <svg class="abs arrow" style="left:30px;top:230px" viewBox="0 0 30 30"><path d="M19 6 10 15l9 9" fill="none" stroke="currentColor" stroke-width="2"/></svg>
  <svg class="abs arrow" style="left:1140px;top:230px" viewBox="0 0 30 30"><path d="m11 6 9 9-9 9" fill="none" stroke="currentColor" stroke-width="2"/></svg>
  <svg class="abs" style="left:0;top:460px" width="1200" height="140" viewBox="0 0 1200 140" preserveAspectRatio="none">
    <path d="M0 70 C300 150 700 40 1200 20 L1200 60 C700 80 320 160 0 110Z" fill="var(--green)"/>
    <path d="M0 95 C320 165 700 70 1200 50 L1200 140 L0 140Z" fill="var(--white)"/>
  </svg>
</section>

<div class="abs title" style="top:700px">
  <div class="display welcome-kicker">— Welcome to —</div>
  <h3 class="display" style="margin-top:4px">Birchwell Chiropractic</h3>
</div>
<div class="abs welcome-copy">
  <h4>Chiropractic care that's so much more than just pain relief</h4>
  <p>Our team builds a plan around your goals, guiding each visit so your body can heal, move freely and stay strong. Small steps taken each week add up to lasting change in how you feel every day.</p>
  <p>We listen first, explain clearly and adjust gently, so you always know what comes next on the road to better health.</p>
  <span class="btn" style="margin-top:22px">Read More</span>
</div>
<div class="abs video" role="img" aria-label="Video still of a human figure with highlighted spine">
  <div class="abs play"></div>
  <svg class="abs" style="left:180px;top:110px" width="16" height="20" viewBox="0 0 16 20"><path d="M0 0 16 10 0 20Z" fill="#fff"/></svg>
  <div class="abs bar"></div>
</div>

<svg class="abs services-bg" viewBox="0 0 1200 820" preserveAspectRatio="none">
  <path d="M0 60 C300 0 800 90 1200 10 L1200 720 C850 820 400 680 0 760Z" fill="var(--blue)"/>
  <path d="M620 800 C850 780 1050 700 1200 640 L1200 670 C1050 740 860 800 620 800Z" fill="var(--green)"/>
</svg>
<div class="abs services-people" role="img" aria-label="Faded photo of smiling patients behind the services"></div>
<div class="abs title" style="top:1226px">
  <h3 class="display" style="color:#fff">Services We Provide</h3>
  <p style="color:rgba(255,255,255,.8)">Gentle, proven care for every stage of life, tailored to your needs and goals.</p>
</div>
<div class="services">
  <div class="abs card" style="left:210px;top:1306px"><div class="ph" role="img" aria-label="Chiropractor adjusting a patient's neck"></div><span>Chiropractic</span></div>
  <div class="abs card" style="left:480px;top:1306px"><div class="ph b" role="img" aria-label="Acupuncture needles on a patient's back"></div><span>Acupuncture</span></div>
  <div class="abs card" style="left:750px;top:1306px"><div class="ph" role="img" aria-label="Practitioner testing a patient's arm strength"></div><span>Applied Kinesiology</span></div>
  <div class="abs card" style="left:210px;top:1517px"><div class="ph b" role="img" aria-label="Patient receiving a back massage"></div><span>Massage</span></div>
  <div class="abs card" style="left:480px;top:1517px"><div class="ph g" role="img" aria-label="Herbal remedies and small white pills"></div><span>Homeopathy</span></div>
  <div class="abs card" style="left:750px;top:1517px"><div class="ph" role="img" aria-label="Patient lying on a spinal decompression table"></div><span>Spinal Decompression</span></div>
</div>
<svg class="abs arrow" style="left:140px;top:1490px" viewBox="0 0 30 30"><path d="M19 6 10 15l9 9" fill="none" stroke="currentColor" stroke-width="2"/></svg>
<svg class="abs arrow" style="left:1030px;top:1490px" viewBox="0 0 30 30"><path d="m11 6 9 9-9 9" fill="none" stroke="currentColor" stroke-width="2"/></svg>
<span class="abs btn-ghost" style="left:556px;top:1736px">View All</span>

<div class="abs title" style="top:1940px">
  <h3 class="display">Conditions <span>We Cure</span></h3>
  <p>Relief for everyday aches and long-term problems, using care that treats the cause.</p>
</div>
<div class="abs cond-circle" role="img" aria-label="Woman running with her spine highlighted in orange, in front of a blue circle"></div>
<div class="abs cond" style="right:723px;top:2058px">Fibromyalgia<i></i></div>
<div class="abs cond" style="right:738px;top:2143px">Headache<i></i></div>
<div class="abs cond" style="right:738px;top:2228px">Lower Back Pain<i></i></div>
<div class="abs cond" style="right:723px;top:2313px">Mid Back Pain<i></i></div>
<div class="abs cond" style="left:700px;top:2058px"><i></i>Knee Pain</div>
<div class="abs cond" style="left:716px;top:2143px"><i></i>Neck Pain</div>
<div class="abs cond" style="left:716px;top:2228px"><i></i>Disc Bulge</div>
<div class="abs cond" style="left:700px;top:2313px"><i></i>Heel Pain</div>

<div class="abs testi-bg"></div>
<div class="abs testi-family" role="img" aria-label="Smiling family of parents and two children"></div>
<h3 class="abs display testi-title">Client <b>Testimonials</b></h3>
<div class="abs quote" style="left:360px;top:2570px"><div class="avatar" role="img" aria-label="Client portrait"></div><div><p>"After a few visits my back felt better than it has in years. Friendly staff."</p><small>Karen L. <em>★★★★★</em></small></div></div>
<div class="abs quote" style="left:660px;top:2570px"><div class="avatar" role="img" aria-label="Client portrait"></div><div><p>"They explained every step and my headaches are finally under control."</p><small>Mark D. <em>★★★★★</em></small></div></div>
<div class="abs quote" style="left:960px;top:2570px;width:230px"><div class="avatar" role="img" aria-label="Client portrait"></div><div><p>"Caring, patient team. I walk without knee pain again."</p><small>Ruth S. <em>★★★★★</em></small></div></div>

<div class="abs doc-photo" role="img" aria-label="Portrait of the chiropractor and his wife"></div>
<div class="abs doc-caption">Dr. Halvorsen &amp; His Wife Anna</div>
<div class="abs doc" style="left:505px;top:2768px;width:500px">
  <h3 class="display">Meet <b>Dr Halvorsen</b></h3>
  <h5>Education</h5>
  <p>Lakemont Chiropractic College, 1992, Doctor of Chiropractic, with Honors</p>
  <h5>Additional Education</h5>
  <div class="edu">
    <div>Certified in spinal rehab and posture care</div>
    <div>Advanced course in sports injury care</div>
    <div>Trained in gentle low force methods</div>
    <div>Nutrition and wellness studies program</div>
  </div>
  <div style="display:flex;gap:90px">
    <div><h5>Licensure</h5><p>State Board of Chiropractic Examiners<br>Regional Board of Chiropractic Examiners</p></div>
    <div><h5>Member</h5><p>State Chiropractic Association</p></div>
  </div>
</div>

<svg class="abs blog-bg" viewBox="0 0 1200 600" preserveAspectRatio="none">
  <path d="M0 40 C350 0 800 80 1200 0 L1200 600 L0 600Z" fill="var(--green)"/>
</svg>
<div class="abs title" style="top:3196px">
  <h3 class="display" style="color:#fff">Latest Blog</h3>
  <p style="color:rgba(255,255,255,.85)">Tips, news and simple steps to help you feel your best between visits.</p>
</div>
<div class="abs post" style="left:210px;top:3286px"><div class="ph" role="img" aria-label="Hands adjusting a patient's spine"><div class="date">28<small>JAN</small></div></div><h6>Should I See A Chiropractor For My Plantar Fasciitis?</h6><p>Heel pain can slow your whole day. Learn how gentle care may help you walk with ease again.</p></div>
<div class="abs post" style="left:480px;top:3286px"><div class="ph b" role="img" aria-label="Patient receiving a neck adjustment"><div class="date">23<small>JAN</small></div></div><h6>Should I See A Chiropractor For My Plantar Fasciitis?</h6><p>Heel pain can slow your whole day. Learn how gentle care may help you walk with ease again.</p></div>
<div class="abs post" style="left:750px;top:3286px"><div class="ph" role="img" aria-label="Therapist working on a patient's shoulder"><div class="date">22<small>JAN</small></div></div><h6>Should I See A Chiropractor For My Plantar Fasciitis?</h6><p>Heel pain can slow your whole day. Learn how gentle care may help you walk with ease again.</p></div>
<svg class="abs arrow" style="left:140px;top:3420px" viewBox="0 0 30 30"><path d="M19 6 10 15l9 9" fill="none" stroke="currentColor" stroke-width="2"/></svg>
<svg class="abs arrow" style="left:1030px;top:3420px" viewBox="0 0 30 30"><path d="m11 6 9 9-9 9" fill="none" stroke="currentColor" stroke-width="2"/></svg>

<div class="abs social" style="left:210px;top:3720px">
  <h4 class="display"><i></i>ZQ</h4>
  <div class="widget" style="margin-top:16px">
    <div class="head">Birchwell Chiropractic</div>
    <div class="row"><b>Birchwell Chiropractic</b><br>New patients welcome this month. Book your first visit online today.</div>
    <div class="row"><b>Birchwell Chiropractic</b><br>Stretch for five minutes each morning to ease stiffness.</div>
    <div class="ph" style="height:120px" role="img" aria-label="Shared photo of a treatment session"></div>
  </div>
</div>
<div class="abs social" style="left:620px;top:3720px">
  <h4 class="display"><i></i>Chirplane</h4>
  <div class="widget" style="margin-top:16px">
    <div class="row" style="display:flex;justify-content:space-between"><b>Birchwell Chiropractic</b><span class="btn" style="padding:3px 12px;font-size:9px">Follow</span></div>
    <div class="row"><b>Birchwell Chiropractic</b><br>Good posture starts with small daily habits. Here are three to try.</div>
    <div class="row"><b>Birchwell Chiropractic</b><br>Thank you to everyone who joined our spine health talk.</div>
    <div class="ph b" style="height:110px" role="img" aria-label="Shared photo of a patient stretching"></div>
  </div>
</div>

<div class="abs map" role="img" aria-label="Street map showing the clinic location"></div>
<svg class="abs footer-bg" viewBox="0 0 1200 480" preserveAspectRatio="none">
  <path d="M0 60 C300 0 800 90 1200 20 L1200 480 L0 480Z" fill="var(--blue)"/>
  <path d="M0 50 C300 -10 800 80 1200 10 L1200 24 C800 96 300 8 0 64Z" fill="var(--green)"/>
</svg>
<div class="abs fcol" style="left:210px;top:4440px">
  <h5>Quick Links</h5>
  <ul><li>Home</li><li>Health Services</li><li>About</li><li>FAQ</li><li>New Patients</li><li>Contact Us</li></ul>
</div>
<div class="abs fcol" style="left:390px;top:4440px;width:190px">
  <h5>Contact Info</h5>
  <div class="ci"><svg width="12" height="14" viewBox="0 0 12 14"><path d="M6 0a5 5 0 0 0-5 5c0 4 5 9 5 9s5-5 5-9a5 5 0 0 0-5-5zm0 7a2 2 0 1 1 0-4 2 2 0 0 1 0 4z" fill="#fff"/></svg><span>2210 Larkspur Avenue<br>Fernhollow, TX 79000</span></div>
  <div class="ci"><svg width="12" height="12" viewBox="0 0 12 12"><path d="M2 0h3l1 3-2 1c1 2 2 3 4 4l1-2 3 1v3l-1 2C5 12 0 7 0 1z" fill="#fff"/></svg><span>555-0142</span></div>
  <div class="ci"><svg width="12" height="12" viewBox="0 0 12 12"><path d="M2 0h3l1 3-2 1c1 2 2 3 4 4l1-2 3 1v3l-1 2C5 12 0 7 0 1z" fill="#fff"/></svg><span>555-0143</span></div>
  <div class="ci"><svg width="12" height="10" viewBox="0 0 12 10"><rect width="12" height="10" fill="#fff"/><path d="M0 0l6 5 6-5" fill="none" stroke="var(--blue)"/></svg><span>info@marvintoque.com</span></div>
</div>
<div class="abs fcol" style="left:600px;top:4440px">
  <h5>Opening Hours</h5>
  <table class="hours">
    <tr><td>Mon</td><td>08:00 - 17:00</td></tr>
    <tr><td>Tue</td><td>08:00 - 17:00</td></tr>
    <tr><td>Wed</td><td>08:00 - 17:00</td></tr>
    <tr><td>Thu</td><td>08:00 - 17:00</td></tr>
    <tr><td>Fri</td><td>08:00 - 17:00</td></tr>
    <tr><td>Sat</td><td>Closed</td></tr>
    <tr><td>Sun</td><td>Closed</td></tr>
  </table>
</div>
<div class="abs fcol" style="left:820px;top:4440px">
  <h5>Follow Us</h5>
  <div class="f-brand"><i></i>Birchwell</div>
  <div class="circles"><i></i><i></i><i></i><i></i></div>
</div>
<div class="abs copyright">© Copyright Birchwell Chiropractic. All rights reserved.</div>

</body>
</html>
```